Website Design - Financial Services Software

We are looking for website designs for our public website.
Some competitor sites we like are
www.torvani.com.au
www.pluma.com.au
www.quentabridge.com
www.morlupa.com.au

A wireframe example of our site can be found at
http://pr4tqz.bivlowpage.com/

Attached is our logo.

Industry/Entity Type

Financial

```html
<!DOCTYPE html>
<html lang="en">
<head>
<meta charset="utf-8">
<title>Veridane – FAQ</title>
<link href="https://fonts.googleapis.com/css2?family=Fenix&display=swap" rel="stylesheet">
<style>
  :root {
    --page-bg: #efeff1;
    --header-dark: #282526;
    --footer-black: #0c0b0b;
    --card-bg: #ffffff;
    --card-border: #e2e2e4;
    --panel-bg: #f0f0f2;
    --accent: #2a94d6;
    --ink: #141213;
    --body-ink: #3a3738;
    --rule: #dcdcde;
    --white: #ffffff;
    --social: #2f7fc1;
  }
  * { box-sizing: border-box; margin: 0; padding: 0; }
  html, body { width: 1010px; height: 1200px; overflow: hidden; background: var(--page-bg); }
  body { font-family: "Fenix", Georgia, serif; color: var(--ink); position: relative; }
  .abs { position: absolute; }

  /* Header */
  .site-header { left: 130px; top: 0; width: 764px; height: 131px; background: var(--header-dark); border-radius: 0 0 6px 6px; }
  .brand-mark { left: 68px; top: 16px; width: 52px; height: 52px; background: var(--white); }
  .brand-name { left: 35px; top: 82px; font-size: 24px; line-height: 28px; letter-spacing: 1px; color: var(--white); }
  .social-square { width: 16px; height: 16px; background: var(--social); top: 18px; }
  .login { left: 692px; top: 19px; font-size: 10px; line-height: 14px; color: var(--white); }
  .login-sep { left: 681px; top: 20px; width: 1px; height: 11px; background: #6b6768; }
  .main-nav a { position: absolute; top: 99px; font-size: 13px; line-height: 18px; color: var(--white); text-decoration: none; }
  .main-nav a.current { color: var(--accent); }
  .nav-sep { top: 101px; width: 1px; height: 14px; background: #6b6768; }

  /* Card */
  .faq-card { left: 130px; top: 141px; width: 764px; height: 919px; background: var(--card-bg); border: 1px solid var(--card-border); border-radius: 8px; }
  .page-title { left: 168px; top: 159px; font-size: 20px; line-height: 24px; color: var(--accent); font-weight: 400; }

  .toc { left: 505px; top: 189px; width: 350px; height: 231px; background: var(--panel-bg); border-radius: 6px; padding: 20px 0 0 33px; }
  .toc h2 { font-size: 16px; line-height: 18px; font-weight: 400; color: var(--accent); margin-bottom: 1px; }
  .toc ol { list-style: none; }
  .toc li { font-size: 12.5px; line-height: 18.7px; color: var(--ink); }

  .faq-item { left: 169px; width: 685px; }
  .faq-item.narrow { width: 322px; }
  .faq-item h3 { font-size: 16px; line-height: 18px; font-weight: 400; letter-spacing: 0.2px; color: var(--ink); }
  .faq-item p { font-size: 10.3px; line-height: 14px; color: var(--body-ink); margin-top: 4px; }
  .faq-item p + p { margin-top: 14px; }
  .rule { height: 1px; background: var(--rule); }

  /* Footer */
  .site-footer { left: 130px; top: 1068px; width: 764px; height: 105px; background: var(--header-dark); border-radius: 6px 6px 0 0; }
  .footer-mark { left: 199px; top: 1086px; width: 44px; height: 44px; background: var(--white); }
  .footer-name { left: 171px; top: 1142px; font-size: 19px; line-height: 22px; letter-spacing: 1px; color: var(--white); }
  .footer-col h4 { font-size: 14px; line-height: 16px; font-weight: 400; color: var(--white); margin-bottom: 2px; }
  .footer-col ul { list-style: none; }
  .footer-col li { font-size: 9.5px; line-height: 17px; color: var(--white); }
  .footer-col li::before { content: "• "; }
  .connect-row { display: flex; align-items: center; gap: 7px; font-size: 9.5px; color: var(--white); height: 17px; }
  .connect-row + .connect-row { margin-top: 7px; }
  .connect-square { width: 17px; height: 17px; background: var(--social); }
  .legal-bar { left: 130px; top: 1173px; width: 764px; height: 27px; background: var(--footer-black); }
  .copyright { left: 41px; top: 7px; font-family: Arial, Helvetica, sans-serif; font-size: 8.5px; color: var(--white); }
</style>
</head>
<body>

<header class="site-header abs">
  <div class="brand-mark abs"></div>
  <div class="brand-name abs">VERIDANE</div>
  <div class="social-square abs" style="left:631px"></div>
  <div class="social-square abs" style="left:656px"></div>
  <div class="login-sep abs"></div>
  <div class="login abs">LOGIN</div>
  <nav class="main-nav">
    <a href="#" style="left:380px">FEATURES</a>
    <span class="nav-sep abs" style="left:467px"></span>
    <a href="#" style="left:492px">EXAMPLES</a>
    <span class="nav-sep abs" style="left:580px"></span>
    <a href="#" class="current" style="left:605px">FAQ</a>
    <span class="nav-sep abs" style="left:655px"></span>
    <a href="#" style="left:679px">ABOUT</a>
  </nav>
</header>

<main>
  <div class="faq-card abs"></div>
  <h1 class="page-title abs">QUESTIONS? WE'VE GOT ANSWERS.</h1>

  <aside class="toc abs">
    <h2>ON THIS PAGE</h2>
    <ol>
      <li>1. What is Veridane</li>
      <li>2. What sort of modelling can I do?</li>
      <li>3. Why would I want to use Veridane?</li>
      <li>4. Is Veridane right for me?</li>
      <li>5. What do I need to use Veridane?</li>
      <li>6. Is my data safe and secure with Veridane?</li>
      <li>7. How much does Veridane cost?</li>
      <li>8. Can I integrate Veridane with my CRM?</li>
      <li>9. Can I use Pluma Cashbooks with Veridane?</li>
    </ol>
  </aside>

  <section class="faq-item narrow abs" style="top:194px">
    <h3>WHAT IS VERIDANE</h3>
    <p>Lorem ipsum dolor sit amet, consectetur adipiscing elit. Morbi dapibus justo vel felis volutpat, sit amet congue arcu lacinia. Aenean elementum hendrerit turpis nec sodales.</p>
    <p>Maecenas vehicula justo et mauris tempus, vel dignissim dolor aliquet. Maecenas erat metus, scelerisque eget placerat gravida, consectetur fermentum magna</p>
  </section>
  <div class="rule abs" style="left:169px;top:329px;width:322px"></div>

  <section class="faq-item narrow abs" style="top:342px">
    <h3>WHAT SORT OF MODELLING CAN I DO?</h3>
    <p>Lorem ipsum dolor sit amet, consectetur adipiscing elit. Morbi dapibus justo vel felis volutpat, sit amet congue arcu lacinia. Aenean elementum hendrerit turpis nec sodales.</p>
    <p>Maecenas vehicula justo et mauris tempus, vel dignissim dolor aliquet. Maecenas erat metus, scelerisque eget placerat gravida, consectetur fermentum magna</p>
  </section>
  <div class="rule abs" style="left:169px;top:475px;width:685px"></div>

  <section class="faq-item abs" style="top:487px">
    <h3>WHY WOULD I WANT TO USE VERIDANE?</h3>
    <p>Lorem ipsum dolor sit amet, consectetur adipiscing elit. Morbi dapibus justo vel felis volutpat, sit amet congue arcu lacinia. Aenean elementum hendrerit turpis nec sodales.</p>
    <p>Maecenas vehicula justo et mauris tempus, vel dignissim dolor aliquet. Maecenas erat metus, scelerisque eget placerat gravida, consectetur fermentum magna</p>
  </section>
  <div class="rule abs" style="left:169px;top:597px;width:685px"></div>

  <section class="faq-item abs" style="top:609px">
    <h3>IS VERIDANE RIGHT FOR ME?</h3>
    <p>Lorem ipsum dolor sit amet, consectetur adipiscing elit. Morbi dapibus justo vel felis volutpat, sit amet congue arcu lacinia. Aenean elementum hendrerit turpis nec sodales.</p>
  </section>
  <div class="rule abs" style="left:169px;top:672px;width:685px"></div>

  <section class="faq-item abs" style="top:682px">
    <h3>WHAT DO I NEED TO USE VERIDANE?</h3>
    <p>Lorem ipsum dolor sit amet, consectetur adipiscing elit. Morbi dapibus justo vel felis volutpat, sit amet congue arcu lacinia. Aenean elementum hendrerit turpis nec sodales.</p>
  </section>
  <div class="rule abs" style="left:169px;top:748px;width:685px"></div>

  <section class="faq-item abs" style="top:759px">
    <h3>IS MY DATA SAFE AND SECURE WITH VERIDANE?</h3>
    <p>Lorem ipsum dolor sit amet, consectetur adipiscing elit. Morbi dapibus justo vel felis volutpat, sit amet congue arcu lacinia. Aenean elementum hendrerit turpis nec sodales.</p>
  </section>
  <div class="rule abs" style="left:169px;top:821px;width:685px"></div>

  <section class="faq-item abs" style="top:832px">
    <h3>HOW MUCH DOES VERIDANE COST?</h3>
    <p>Lorem ipsum dolor sit amet, consectetur adipiscing elit. Morbi dapibus justo vel felis volutpat, sit amet congue arcu lacinia. Aenean elementum hendrerit turpis nec sodales.</p>
  </section>
  <div class="rule abs" style="left:169px;top:894px;width:685px"></div>

  <section class="faq-item abs" style="top:905px">
    <h3>CAN I INTEGRATE VERIDANE WITH MY CRM?</h3>
    <p>Lorem ipsum dolor sit amet, consectetur adipiscing elit. Morbi dapibus justo vel felis volutpat, sit amet congue arcu lacinia. Aenean elementum hendrerit turpis nec sodales.</p>
  </section>
  <div class="rule abs" style="left:169px;top:976px;width:685px"></div>

  <section class="faq-item abs" style="top:987px">
    <h3>CAN I USE PLUMA CASHBOOKS WITH VERIDANE?</h3>
    <p>Lorem ipsum dolor sit amet, consectetur adipiscing elit. Morbi dapibus justo vel felis volutpat, sit amet congue arcu lacinia. Aenean elementum hendrerit turpis nec sodales.</p>
  </section>
</main>

<footer>
  <div class="site-footer abs"></div>
  <div class="footer-mark abs"></div>
  <div class="footer-name abs">VERIDANE</div>

  <div class="footer-col abs" style="left:333px;top:1090px">
    <h4>ABOUT</h4>
    <ul><li>About Us</li><li>Support</li></ul>
  </div>
  <div class="footer-col abs" style="left:433px;top:1090px">
    <h4>GETTING STARTED</h4>
    <ul><li>Why Veridane</li><li>Download a Summary</li><li>Veridane Videos</li></ul>
  </div>
  <div class="footer-col abs" style="left:597px;top:1090px">
    <h4>LEGAL</h4>
    <ul><li>Terms of Use</li><li>Privacy</li></ul>
  </div>
  <div class="footer-col abs" style="left:707px;top:1090px">
    <h4>CONNECT</h4>
    <div class="connect-row"><span class="connect-square"></span>VERIDANE ON LINKORA</div>
    <div class="connect-row"><span class="connect-square"></span>VERIDANE ON CHIRPNET</div>
  </div>

  <div class="legal-bar abs">
    <div class="copyright abs">Copyright © 2014 Veridane Pty Ltd. All rights reserved.</div>
  </div>
</footer>

</body>
</html>
```